Business Card Design For Tidecrest Audio

Tidecrest Audio is a small pro-audio company providing rental and install services for professional sound reinforcement. Focus is gigs (any gigs) needing high quality audio; from corporate to chamber music to hard hitting rock.

Tidecrest Audio
Pro-audio for your gig ... spine-tingle good
Doran Pelley
doran@tidecrestaudio.example.com.au
0482 356 071

We need a business card design and an "drop-off"' larger card (eg. one third A4 size: 99mm wide x 210mm high) with more details.
Updates

Please note I've had limited internet access for last few days and for the next four.  The work so far looks great .. I'll provide some individual feedback on the designs now.  Great work, many thanks, love the creativity!

Doran

Industry/Entity Type

Business

```html
<!DOCTYPE html>
<html lang="en">
<head>
<meta charset="utf-8">
<title>Tidecrest Audio — Business Card</title>
<link rel="stylesheet" href="https://fonts.googleapis.com/css2?family=Delius&family=Special+Elite&display=block">
<style>
  :root {
    --ink: #141414;
    --peach: #f0956e;
    --orange: #f4a641;
    --yellow: #e9dc4a;
    --lime: #b9dc4c;
    --green: #3dbb6a;
    --teal: #1aa88c;
    --card-w: 1200px;
    --card-h: 693px;
  }
  html, body {
    margin: 0;
    padding: 0;
    width: var(--card-w);
    height: var(--card-h);
    overflow: hidden;
    background: #ffffff;
  }
  .business-card {
    position: relative;
    width: var(--card-w);
    height: var(--card-h);
    overflow: hidden;
    color: var(--ink);
  }
  .streak-backdrop {
    position: absolute;
    inset: 0;
    background:
      linear-gradient(62deg, rgba(255,255,255,0.14) 0%, rgba(255,255,255,0) 18%, rgba(255,255,255,0.12) 36%, rgba(255,255,255,0) 52%, rgba(255,255,255,0.14) 70%, rgba(255,255,255,0) 88%),
      linear-gradient(118deg, var(--peach) 0%, var(--orange) 24%, var(--yellow) 44%, var(--lime) 58%, var(--green) 80%, var(--teal) 100%);
  }
  .brand {
    position: absolute;
    left: 0;
    right: 0;
    top: 28px;
    text-align: center;
  }
  .brand-name {
    margin: 0;
    font-family: "Delius", sans-serif;
    font-weight: 400;
    font-size: 150px;
    line-height: 1;
    letter-spacing: 1px;
    white-space: nowrap;
  }
  .tagline {
    position: absolute;
    right: 50px;
    top: 186px;
    margin: 0;
    font-family: "Delius", sans-serif;
    font-size: 46px;
    line-height: 1;
    white-space: nowrap;
  }
  .contact {
    position: absolute;
    left: 0;
    right: 0;
    top: 445px;
    text-align: center;
    font-family: "Special Elite", "Courier New", monospace;
  }
  .contact-name {
    margin: 0 0 10px;
    padding-right: 60px;
    font-size: 86px;
    font-weight: 400;
    line-height: 1;
    white-space: nowrap;
  }
  .contact-line {
    margin: 0;
    font-size: 40px;
    line-height: 1.3;
    white-space: nowrap;
  }
  .contact-phone {
    font-size: 46px;
  }
</style>
</head>
<body>
  <main class="business-card">
    <div class="streak-backdrop" role="img" aria-label="Diagonal streaked colour wash blending from peach and orange through yellow to green and teal"></div>

    <header class="brand">
      <h1 class="brand-name">Tidecrest Audio</h1>
    </header>
    <p class="tagline">Pro-audio for your gig ... spine-tingle good</p>

    <section class="contact">
      <h2 class="contact-name">Doran Pelley</h2>
      <p class="contact-line contact-email">doran@tidecrestaudio.example.com.au</p>
      <p class="contact-line contact-phone">0482 356 071</p>
    </section>
  </main>
</body>
</html>
```